Cosmetic jar labels,round and wrap around

Hi just starting a small attempt to sell shear butter, with divert flavor all organic and will old Africa formula, would like a wrap around the bottle and also one for the round lid that would have the fragrances name on it , kind of new at this game

Logo Text

Kelavu Oganics by Teresa,from the pearl of Africa(Uganda)

```html
<!DOCTYPE html>
<html lang="en">
<head>
<meta charset="utf-8">
<title>Kelavu Organics Cosmetics – Jar Labels</title>
<link href="https://fonts.googleapis.com/css2?family=Montserrat:wght@400;500;700&display=swap" rel="stylesheet">
<style>
  :root {
    --gold: #b8841f;
    --gold-soft: #a88a4e;
    --sand: #c6b08c;
    --ink: #0d0d0d;
    --paper: #ffffff;
    --cream: #f6f2ea;
  }
  * { margin: 0; padding: 0; box-sizing: border-box; }
  html, body { width: 1152px; height: 1200px; overflow: hidden; }
  body {
    background: var(--sand);
    font-family: "Montserrat", sans-serif;
    position: relative;
  }
  .top-band {
    position: absolute; left: 0; top: 0; width: 1152px; height: 40px;
    background: var(--gold);
  }
  .pattern-strip {
    position: absolute; left: 0; top: 40px; width: 1152px; height: 82px;
    background: linear-gradient(180deg, #fff 0 4px, #8e7a55 4px calc(100% - 4px), #fff calc(100% - 4px));
  }
  .lid-label { position: absolute; left: 71px; top: 468px; }
  .wrap-label { position: absolute; left: 408px; top: 523px; }
  .brand { font-family: "Montserrat", sans-serif; font-weight: 700; fill: var(--gold); }
  .caption { font-family: "Montserrat", sans-serif; font-weight: 500; fill: var(--paper); letter-spacing: 1.5px; }
  .origin { font-family: "Montserrat", sans-serif; font-weight: 400; fill: var(--ink); }
</style>
</head>
<body>
  <div class="top-band"></div>
  <div class="pattern-strip" role="img" aria-label="Band of gold and black dot pattern"></div>

  <svg class="lid-label" width="304" height="304" viewBox="-152 -152 304 304" aria-label="Round lid label">
    <circle r="152" fill="var(--gold)"/>
    <circle r="137" fill="none" stroke="var(--paper)" stroke-width="0.8" stroke-dasharray="3 3"/>
    <circle r="120" fill="var(--cream)"/>
    <circle r="117" fill="none" stroke="var(--gold)" stroke-width="2.4" stroke-dasharray="0.1 5" stroke-linecap="round"/>
    <text class="brand" x="0" y="-74" text-anchor="middle" font-size="25" letter-spacing="2">KELAVU</text>
    <text class="brand" x="0" y="-54" text-anchor="middle" font-size="15.5" letter-spacing="0.5">ORGANICS</text>
    <text class="brand" x="0" y="-37" text-anchor="middle" font-size="15.5" letter-spacing="0.5">COSMETICS</text>
    <text class="brand" x="0" y="-8" text-anchor="middle" font-size="14">by Teresa</text>
    <path d="M -87 18 L 87 18 A 87 50 0 0 1 -87 18 Z" fill="var(--ink)"/>
    <text class="caption" x="0" y="38" text-anchor="middle" font-size="11">SHEA</text>
    <text class="caption" x="0" y="52" text-anchor="middle" font-size="11">BUTTER</text>
    <line x1="-12" y1="59" x2="12" y2="59" stroke="var(--gold)" stroke-width="1"/>
    <defs>
      <path id="origin-arc" d="M -108 0 A 108 108 0 0 0 108 0"/>
    </defs>
    <text class="origin" font-size="7.5" letter-spacing="3.2">
      <textPath href="#origin-arc" startOffset="50%" text-anchor="middle">FROM THE PEARL OF AFRICA -UGANDA-</textPath>
    </text>
  </svg>

  <svg class="wrap-label" width="648" height="195" viewBox="0 0 648 195" aria-label="Wrap-around jar label">
    <rect width="648" height="195" fill="var(--cream)"/>
    <rect width="648" height="9" fill="var(--gold)"/>
    <rect y="9" width="648" height="38" fill="#8e7a55" role="img" aria-label="Gold and black dot pattern strip"/>
    <rect x="255" y="0" width="138" height="47" fill="var(--ink)"/>
    <line x1="316" y1="20" x2="332" y2="20" stroke="var(--gold)" stroke-width="1"/>
    <text class="caption" x="324" y="39" text-anchor="middle" font-size="12">SHEA BUTTER</text>
    <text class="brand" x="324" y="84" text-anchor="middle" font-size="30" letter-spacing="3">KELAVU</text>
    <text class="brand" x="324" y="104" text-anchor="middle" font-size="18" letter-spacing="0.6">ORGANICS COSMETICS</text>
    <text class="brand" x="324" y="146" text-anchor="middle" font-size="17">by Teresa</text>
    <text class="origin" x="324" y="171" text-anchor="middle" font-size="7.5" letter-spacing="4">FROM THE PEARL OF AFRICA -UGANDA-</text>
    <rect y="184" width="648" height="11" fill="var(--gold)"/>
  </svg>
</body>
</html>
```